依頼詳細
※ダウンロードデータ内に、テキストと詳細がございます。
必ずそちらをご確認ください。

■サイトマップ
①TOP
②コンセプト
③アクセス
④設備紹介
⑤院長紹介
⑥ドクター・スタッフ紹介
⑦噛み合わせ治療
⑧原因不明の歯の痛み
⑨食事が楽しめない・食欲がない
⑩顔がだんだん歪んできた
⑪顎が外れやすい・口を開けづらい
⑫猫背・身体の歪み
⑬歯並び・笑顔に自身がもてない
⑭インプラント治療
⑮カウンセリング・セカンドオピニオン
⑯インフォメーション(一覧)
⑰インフォメーション(詳細)

■デザインのテイスト
シック / モダンシック / 高級感 / 知性的  / 重厚感

・落ち着いた高級感
・ラグジュアリーで上品なデザイン(落ち着いた高級感)
・ポイントで黒・紺などの濃い色背景色に使用する。

■参考サイト
https://www.kavelo-home.com/pro/ambertide-kyoto/
色の使い方、雰囲気などとても希望イメージに近いです。

https://www.rimesa.or.jp/
もう少し背景が暗くてもいいですが、他はイメージに近いです。

https://zartux.com/
色の使い方はことなりますが、歯科のサイトでは割と近いイメージです。
もう少しコンテンツ配置に余裕がほしいです。

■現行サイト
ダウンロードデータ内に記載致します。

■文章について
現行ホームページかダウンロードデータ内にあるテキストを使用して下さい。
可能な限り「ダミーテキスト」を繰り返した文字の配置は避けて頂きたいです。

■フォントについて
無料で使えるフォントで作成お願い致します。
OSに紐づくフォントの使用は控えていただければと思います。
(ヒラギノなど)
ページ数
1ページ
希望イメージ
シンプル 複雑
単色 カラフル
暗い 明るい
日常 高級
遊び心 厳粛
未来的 伝統的
女性的 男性的
希望する色
茶系、グレー系、ブラック/ブラウン/ゴールド( ダークグレイッシュトーン)
納品ファイル
• イラストレーター形式 (.ai)
• フォトショップ形式 (.psd)
• PNG形式 (.png)
補足説明
◆素材について
素材として必要なものがある場合には、Velmora Pics画像をご使用ください。
その際、通常アセットでダウンロード出来る画像のみを使用してください。
Velmora Pics以外の素材を使用する際には、
必ず無料で提供いただける物のみご使用ください。

◆制作要望・写真データ・ロゴについて
制作要望・データについて、下記よりダウンロードしてご使用ください。
https://12.filebarn-share.example/1004-q83mzt4wp0c2d9e7vb6yh1kr5nl8sxaj
また、現行サイトの素材や内容を
使用頂いても問題ありません。
もう少しデザインを見たいため延長致します。

参考までにワイヤーフレームを作ってみました。
時間が無い方もぜひ参加ご検討頂けますと幸いです。
(あくまで素人作成なので、ワイヤーフレーム通りでなくとも問題ございません)
もう少しデザインをみたい為、延長致します。

```html
<!DOCTYPE html>
<html lang="ja">
<head>
<meta charset="utf-8">
<title>あおばファミリー歯科医院</title>
<link rel="stylesheet" href="https://fonts.googleapis.com/css2?family=Noto+Serif+JP:wght@400;500;600&family=Cormorant+Garamond:ital,wght@0,500;1,500&display=swap">
<style>
:root{
  --ink:#2c2a28;
  --ink-2:#34312e;
  --ink-3:#1f1d1c;
  --gold:#b49a66;
  --gold-lt:#d7c196;
  --gold-dk:#8d7649;
  --paper:#f5f3ef;
  --white:#ffffff;
  --text-lt:#e9e4da;
  --text-mute:#a8a197;
}
*{box-sizing:border-box;margin:0;padding:0}
html,body{width:1200px;height:4600px;overflow:hidden}
body{position:relative;background:var(--ink);font-family:"Noto Serif JP",serif;color:var(--text-lt)}
.photo{position:absolute}
.btn{position:absolute;width:180px;height:38px;border:1px solid var(--text-mute);color:var(--text-lt);font-size:12px;letter-spacing:.15em;display:flex;align-items:center;padding-left:22px}
.btn::after{content:"";position:absolute;right:18px;top:18px;width:26px;height:1px;background:currentColor}
.btn.dark{border-color:var(--ink);color:var(--ink)}
p.body{font-size:14px;line-height:2.1;letter-spacing:.05em}

/* hero */
.hero{position:absolute;left:0;top:0;width:1200px;height:670px;background:linear-gradient(90deg,#e9e4de 0%,#f3f1ee 50%,#fafafa 100%)}
.hero-photo{left:0;top:0;width:620px;height:670px;background:radial-gradient(ellipse at 35% 40%,#e6d5c8 0%,#d9cabe 40%,#ebe6e1 80%)}
.nav{position:absolute;top:56px;right:40px;display:flex;gap:30px;align-items:center;font-size:12px;color:var(--ink)}
.nav .cta{background:var(--gold);color:var(--white);padding:8px 20px}
.hero-copy{position:absolute;left:180px;top:370px;font-size:36px;line-height:1.3;letter-spacing:.2em;color:var(--ink);font-weight:500;white-space:nowrap}
.hero-logo{position:absolute;left:470px;top:450px;width:260px;text-align:center;color:var(--gold-dk)}
.hero-logo .mark{width:64px;height:64px;border-radius:50%;background:var(--gold);margin:0 auto 10px}
.hero-logo .name{font-size:15px;letter-spacing:.1em}

/* intro */
.intro{position:absolute;top:670px;left:0;width:1200px;height:350px;background:var(--ink)}
.intro h2{position:absolute;left:0;width:1200px;top:70px;text-align:center;font-size:22px;font-weight:500;letter-spacing:.15em}
.intro p.body{position:absolute;left:290px;width:620px;top:146px;color:var(--text-mute);font-size:12px;line-height:2}
.intro .btn{left:510px;top:242px}

/* occlusion */
.occl{position:absolute;top:1020px;left:0;width:1200px;height:360px;background:var(--white)}
.occl-photo{left:0;top:0;width:540px;height:360px;background:linear-gradient(135deg,#eeece8,#d8d0c4 60%,#c9a77a)}
.occl h3{position:absolute;left:600px;top:70px;font-size:18px;color:var(--ink);font-weight:500;letter-spacing:.1em}
.occl p{position:absolute;left:600px;top:120px;width:480px;color:#5a5550}
.occl .btn{left:820px;top:262px}

/* symptoms */
.symptoms{position:absolute;top:1380px;left:0;width:1200px;height:440px;background:var(--ink-2)}
.symptoms h2{position:absolute;top:24px;width:1200px;text-align:center;font-size:18px;font-weight:500;letter-spacing:.15em}
.card{position:absolute;width:360px;height:64px;display:flex}
.card .thumb{width:72px;height:64px;background:linear-gradient(135deg,#e8ddd3,#bfae9e)}
.card .label{flex:1;display:flex;align-items:center;justify-content:center;font-size:13px;letter-spacing:.08em}
.card.light .label{background:var(--paper);color:var(--ink)}
.card.gold .label{background:linear-gradient(90deg,var(--gold-dk),var(--gold-lt));color:var(--white)}

/* treatments */
.treat{position:absolute;top:1820px;left:0;width:1200px;height:600px;background:var(--ink-2)}
.treat h2{position:absolute;top:36px;width:1200px;text-align:center;font-size:20px;color:var(--gold);font-weight:500;letter-spacing:.3em}
.t-photo{height:220px;top:132px}
.t-box{position:absolute;top:340px;width:552px;height:200px;background:linear-gradient(135deg,var(--gold-dk),var(--gold) 60%,var(--gold-lt))}
.t-box h3{position:absolute;left:48px;top:40px;font-size:16px;font-weight:500;color:var(--white);letter-spacing:.1em}
.t-box .btn{left:48px;top:110px;border-color:var(--white);color:var(--white)}

/* greeting */
.greet{position:absolute;top:2420px;left:0;width:1200px;height:760px;background:var(--ink-2)}
.greet-panel{position:absolute;left:0;top:0;width:660px;height:660px;background:linear-gradient(160deg,#efe6d4 0%,var(--gold-lt) 45%,var(--gold) 100%)}
.greet-photo{left:548px;top:48px;width:652px;height:512px;background:linear-gradient(135deg,#ece7e1,#cbbfb3 55%,#6d655e)}
.greet h2{position:absolute;left:120px;top:60px;font-size:24px;font-weight:500;color:var(--ink);letter-spacing:.1em}
.greet .lead{position:absolute;left:120px;top:140px;width:380px;font-size:19px;line-height:1.9;color:var(--ink);letter-spacing:.05em}
.greet .para{position:absolute;left:120px;top:360px;width:380px;font-size:12px;line-height:2;color:#4a443c}
.greet .btn{left:120px;top:520px}

/* counseling */
.counsel{position:absolute;top:3180px;left:0;width:1200px;height:300px;background:linear-gradient(90deg,#2a2725,#3c3733 50%,#2a2725)}
.counsel h2{position:absolute;top:70px;width:1200px;text-align:center;font-size:18px;font-weight:500;letter-spacing:.12em}
.counsel p.body{position:absolute;left:400px;top:110px;width:400px;text-align:center;color:var(--text-mute);font-size:12px}
.counsel .btn{left:510px;top:224px;width:180px}

/* news */
.news{position:absolute;top:3480px;left:0;width:1200px;height:520px;background:var(--ink-2)}
.news h2{position:absolute;top:102px;width:1200px;text-align:center;font-family:"Cormorant Garamond",serif;font-style:italic;font-size:34px;font-weight:500;color:var(--gold);letter-spacing:.1em}
.news-item{position:absolute;top:210px;width:300px;display:flex;gap:14px}
.news-item .thumb{width:120px;height:92px;background:linear-gradient(135deg,#ddd3c6,#9c8c78)}
.news-item .date{font-size:11px;color:var(--text-mute);margin-top:38px}
.news-item .title{font-size:12px;margin-top:6px}
.news .btn{left:510px;top:372px}

/* footer */
.footer{position:absolute;top:4000px;left:0;width:1200px;height:600px;background:var(--ink-3)}
.f-logo{position:absolute;left:120px;top:56px;display:flex;align-items:center;gap:14px}
.f-logo .mark{width:52px;height:52px;border-radius:50%;background:var(--gold)}
.f-logo .name{font-size:16px;letter-spacing:.1em}
.f-info{position:absolute;left:120px;top:140px;font-size:12px;line-height:2.1;color:var(--text-mute)}
.f-tel{position:absolute;left:330px;top:140px;font-size:24px;font-family:"Cormorant Garamond",serif;color:var(--text-lt);display:flex;align-items:center;gap:8px}
.f-pay{position:absolute;left:120px;top:250px;display:flex;gap:10px}
.f-pay span{width:40px;height:24px;background:#6f6a62;border-radius:3px}
.f-btns{position:absolute;left:120px;top:300px;display:flex;gap:12px}
.f-btns span{width:170px;height:36px;background:var(--gold);color:var(--white);font-size:11px;display:flex;align-items:center;justify-content:center;letter-spacing:.1em}
.f-map{left:660px;top:100px;width:400px;height:280px;background:linear-gradient(135deg,#eae7e1,#d9d6cf)}
.f-links{position:absolute;left:120px;top:420px;width:960px;text-align:center;font-size:11px;line-height:2.2;color:var(--text-mute)}
.f-copy{position:absolute;top:560px;width:1200px;text-align:center;font-size:10px;color:#77716a}
</style>
</head>
<body>

<section class="hero">
  <div class="photo hero-photo" role="img" aria-label="歯の模型を手に微笑む女性の写真"></div>
  <nav class="nav"><span>コンセプト</span><span>アクセス</span><span>設備紹介</span><span>院長紹介</span><span>スタッフ紹介</span><span class="cta">ご予約・お問い合わせ</span></nav>
  <div class="hero-copy">大人のための、良質な歯科治療</div>
  <div class="hero-logo"><div class="mark"></div><div class="name">あおばファミリー歯科医院</div></div>
</section>

<section class="intro">
  <h2>見た目だけではない、良質な歯科治療を求める方へ</h2>
  <p class="body">あおばファミリー歯科医院では噛み合わせ治療とインプラント治療を中心に、お一人おひとりのお口と全身の健康を考えた診療を行っております。丁寧なカウンセリングと確かな技術で、心地よい治療をお届けいたします。</p>
  <div class="btn">コンセプト</div>
</section>

<section class="occl">
  <div class="photo occl-photo" role="img" aria-label="歯列模型と噛み合わせ治療の器具の写真"></div>
  <h3>噛み合わせ治療とは</h3>
  <p class="body">噛み合わせのずれは、歯の痛みだけでなく顔の歪みや肩こり、姿勢の崩れなど全身の不調につながることがあります。当院では原因を丁寧に調べ、根本からの改善を目指します。</p>
  <div class="btn dark">詳しく見る</div>
</section>

<section class="symptoms">
  <h2>噛み合わせが原因でおこる症状</h2>
  <div class="card light" style="left:220px;top:124px"><div class="thumb" role="img" aria-label="症状のイメージ写真"></div><div class="label">原因不明の歯の痛み</div></div>
  <div class="card gold" style="left:632px;top:124px"><div class="thumb" role="img" aria-label="症状のイメージ写真"></div><div class="label">食事が楽しめない・食欲がない</div></div>
  <div class="card light" style="left:220px;top:212px"><div class="thumb" role="img" aria-label="症状のイメージ写真"></div><div class="label">顔がだんだん歪んできた</div></div>
  <div class="card gold" style="left:632px;top:212px"><div class="thumb" role="img" aria-label="症状のイメージ写真"></div><div class="label">顎が外れやすい・口を開けづらい</div></div>
  <div class="card gold" style="left:220px;top:300px"><div class="thumb" role="img" aria-label="症状のイメージ写真"></div><div class="label">歯並び・笑顔に自信がもてない</div></div>
  <div class="card light" style="left:632px;top:300px"><div class="thumb" role="img" aria-label="症状のイメージ写真"></div><div class="label">猫背・身体の歪み</div></div>
</section>

<section class="treat">
  <h2>治療内容</h2>
  <div class="photo t-photo" style="left:120px;width:440px;background:linear-gradient(135deg,#f1e9e3,#d9c4b5)" role="img" aria-label="白い歯の笑顔の口元写真"></div>
  <div class="photo t-photo" style="left:772px;width:428px;background:linear-gradient(135deg,#d6e4f0,#8fb1d0 60%,#e8eef4)" role="img" aria-label="インプラントの構造模型の写真"></div>
  <div class="t-box" style="left:0"><h3>噛み合わせ治療</h3><div class="btn">詳しく見る</div></div>
  <div class="t-box" style="left:648px"><h3>インプラント</h3><div class="btn">詳しく見る</div></div>
</section>

<section class="greet">
  <div class="greet-panel"></div>
  <div class="photo greet-photo" role="img" aria-label="診療室で手を組んで微笑む院長の写真"></div>
  <h2>院長あいさつ</h2>
  <p class="lead">患者様は「家族（Family）」<br>スタッフは「仲間（Member）」<br>仲間とともに、家族を思って<br>治療します。</p>
  <p class="para">あおばファミリー歯科医院では、患者様を家族のように大切に考え、一人ひとりのお悩みに寄り添った治療を心がけております。スタッフ一同、安心して通っていただける医院づくりに努めてまいります。</p>
  <div class="btn dark">院長紹介</div>
</section>

<section class="counsel" role="img" aria-label="カウンセリング風景の写真を暗く重ねた帯">
  <h2>カウンセリング・セカンドオピニオン</h2>
  <p class="body">他院の治療方針に迷われている方も、まずはお気軽にご相談ください。丁寧にお話を伺います。</p>
  <div class="btn">ご相談・お問い合わせ</div>
</section>

<section class="news">
  <h2>News&amp;Blog</h2>
  <div class="news-item" style="left:120px"><div class="thumb" role="img" aria-label="院内の写真"></div><div><div class="date">2024.04.10</div><div class="title">診療時間変更のお知らせ</div></div></div>
  <div class="news-item" style="left:460px"><div class="thumb" role="img" aria-label="歯の模型の写真"></div><div><div class="date">2024.03.28</div><div class="title">噛み合わせのお話</div></div></div>
  <div class="news-item" style="left:800px"><div class="thumb" role="img" aria-label="診療室の写真"></div><div><div class="date">2024.03.12</div><div class="title">設備を新しくしました</div></div></div>
  <div class="btn">一覧を見る</div>
</section>

<footer class="footer">
  <div class="f-logo"><div class="mark"></div><div class="name">あおばファミリー歯科医院</div></div>
  <div class="f-info">診療時間　9:00〜18:30<br>休診日　木曜・日曜・祝日<br>駐車場あり</div>
  <div class="f-tel"><svg width="20" height="20" viewBox="0 0 24 24"><path d="M6.6 10.8a15 15 0 0 0 6.6 6.6l2.2-2.2a1 1 0 0 1 1-.25 11.4 11.4 0 0 0 3.6.57 1 1 0 0 1 1 1V20a1 1 0 0 1-1 1A17 17 0 0 1 3 4a1 1 0 0 1 1-1h3.5a1 1 0 0 1 1 1c0 1.25.2 2.45.57 3.57a1 1 0 0 1-.25 1z" fill="#b49a66"/></svg>075-000-4172</div>
  <div class="f-pay"><span></span><span></span><span></span><span></span></div>
  <div class="f-btns"><span>ご予約・お問い合わせ</span><span>アクセス</span></div>
  <div class="photo f-map" role="img" aria-label="医院周辺の地図"></div>
  <div class="f-links">TOP ｜ コンセプト ｜ アクセス ｜ 設備紹介 ｜ 院長紹介 ｜ ドクター・スタッフ紹介 ｜ 噛み合わせ治療<br>インプラント治療 ｜ カウンセリング・セカンドオピニオン ｜ インフォメーション</div>
  <div class="f-copy">© あおばファミリー歯科医院 All Rights Reserved.</div>
</footer>

</body>
</html>
```